Tarrow Building Ventures needs a Business card design and logo

We Need a business card design and logo for a Building & Construction business based in Melbourne. We work in both the Domestic & Commercial sector. We specialize in all aspects of building including extensions, Renovations, and alterations. Construction Management, Project Management, And labour hire
Updates

Industry/Entity Type

Business

```html
<!DOCTYPE html>
<html lang="en">
<head>
<meta charset="utf-8">
<title>Tarrow Building Ventures – Business Card</title>
<link href="https://fonts.googleapis.com/css2?family=Didact+Gothic&display=swap" rel="stylesheet">
<style>
  :root {
    --sky: #2f9ad8;
    --navy: #1e2257;
    --ink: #2a2d4a;
    --paper: #ffffff;
    --backdrop-light: #f1f1f1;
    --backdrop-dark: #c9c9c9;
  }
  * { box-sizing: border-box; margin: 0; padding: 0; }
  html, body { width: 1200px; height: 787px; overflow: hidden; }
  body {
    background: radial-gradient(ellipse at 50% 35%, var(--backdrop-light) 0%, var(--backdrop-dark) 100%);
    font-family: "Didact Gothic", "Century Gothic", sans-serif;
    position: relative;
  }
  .card {
    position: absolute;
    left: 220px; top: 174px;
    width: 760px; height: 440px;
    background: var(--paper);
    box-shadow: 0 6px 18px rgba(0,0,0,.18);
    overflow: hidden;
  }
  .card__top-rule {
    position: absolute; left: 0; right: 0; top: 0;
    height: 7px; background: var(--navy);
  }
  .card__top-band {
    position: absolute; left: 0; right: 0; top: 7px;
    height: 8px; background: var(--sky);
  }
  .card__bottom-band {
    position: absolute; left: 0; right: 0; bottom: 0;
    height: 26px; display: flex;
  }
  .card__bottom-band .band-sky { flex: 0 0 59%; background: var(--sky); }
  .card__bottom-band .band-navy { flex: 1; background: var(--navy); }

  .holder {
    position: absolute; left: 156px; top: 58px;
  }
  .holder__name {
    color: var(--sky);
    font-size: 27px; letter-spacing: 1px;
    font-weight: 400;
  }
  .holder__role {
    color: var(--ink);
    font-size: 15px; margin-top: 6px;
  }

  .brand {
    position: absolute; left: 430px; top: 58px;
    display: flex; align-items: center; gap: 14px;
  }
  .brand__mark {
    width: 56px; height: 56px; background: var(--sky);
  }
  .brand__name {
    color: var(--navy);
    font-size: 22px; line-height: 1.15;
    width: 180px;
  }

  .contacts {
    position: absolute; left: 142px; top: 300px;
    display: flex; gap: 34px;
    font-size: 14px; color: var(--ink);
  }
  .contacts__col { display: flex; flex-direction: column; gap: 10px; }
  .contact { display: flex; align-items: flex-start; gap: 10px; line-height: 1.25; }
  .contact svg { flex: 0 0 auto; width: 17px; height: 17px; }
  .contacts__col--address { width: 145px; }
</style>
</head>
<body>
  <article class="card">
    <div class="card__top-rule"></div>
    <div class="card__top-band"></div>

    <header class="holder">
      <h1 class="holder__name">DANIEL HARGREAVE</h1>
      <p class="holder__role">Managing Director</p>
    </header>

    <div class="brand">
      <span class="brand__mark"></span>
      <span class="brand__name">Tarrow Building Ventures</span>
    </div>

    <section class="contacts">
      <div class="contacts__col contacts__col--address">
        <div class="contact">
          <svg viewBox="0 0 24 24" aria-hidden="true"><path fill="#2f9ad8" d="M12 2a7 7 0 0 0-7 7c0 5 7 13 7 13s7-8 7-13a7 7 0 0 0-7-7zm0 9.5A2.5 2.5 0 1 1 12 6.5a2.5 2.5 0 0 1 0 5z"/></svg>
          <span>Melbourne<br>48 Keel Street<br>Victoria Australia.</span>
        </div>
      </div>
      <div class="contacts__col">
        <div class="contact">
          <svg viewBox="0 0 24 24" aria-hidden="true"><circle cx="12" cy="12" r="10" fill="none" stroke="#2f9ad8" stroke-width="2"/><path fill="#2f9ad8" d="M8.5 7l2 2-1 1.5a6 6 0 0 0 4 4l1.5-1 2 2-1.5 1.5c-3.5 0-8-4.5-8-8z"/></svg>
          <span>021-5550148</span>
        </div>
        <div class="contact">
          <svg viewBox="0 0 24 24" aria-hidden="true"><rect x="7" y="2" width="10" height="20" rx="2" fill="#2f9ad8"/><rect x="9" y="5" width="6" height="11" fill="#fff"/></svg>
          <span>0300-5550192</span>
        </div>
      </div>
      <div class="contacts__col">
        <div class="contact">
          <svg viewBox="0 0 24 24" aria-hidden="true"><rect x="2" y="5" width="20" height="14" fill="none" stroke="#1e2257" stroke-width="2"/><path d="M2 5l10 8 10-8" fill="none" stroke="#1e2257" stroke-width="2"/></svg>
          <span>info@tarrowbv.com</span>
        </div>
        <div class="contact">
          <svg viewBox="0 0 24 24" aria-hidden="true"><circle cx="12" cy="12" r="10" fill="#2f9ad8"/><path d="M2 12h20M12 2c3 3 3 17 0 20M12 2c-3 3-3 17 0 20" fill="none" stroke="#fff" stroke-width="1.4"/></svg>
          <span>www.tarrowbv.com</span>
        </div>
      </div>
    </section>

    <div class="card__bottom-band">
      <span class="band-sky"></span>
      <span class="band-navy"></span>
    </div>
  </article>
</body>
</html>
```